Brightleaf Practice Partners, Inc (www.brightleafpracticepartnrs.example) would like to design a website to convey a level of professionalism to healthcare providers that we are the place form them to visit for Contin. Education, Marketing and Management, Joint Venture Partnerships, etc.
We think we would like a WP Site so that we can use the dynamic and static sides of it's capabilities. We also want to have something that acts as a membership side where members can post their Bio and CV's and prospective employers can post help wanted ads.

Target Market(s)

Pediatricians, Pediatric Dentist, Employers seeking these doctors

Industry/Entity Type

Healthcare

Requirements
Must have
• Services:
Resumes/Bio
Help Wanted
Continuing Education Programs
Marketing & Management

```html
<!DOCTYPE html>
<html lang="en">
<head>
<meta charset="utf-8">
<title>Brightleaf Practice Partners, Inc</title>
<link href="https://fonts.googleapis.com/css2?family=Roboto+Condensed:wght@400;700&display=swap" rel="stylesheet">
<style>
:root{
  --bar:#4a4a4a;
  --bar-dark:#3a3a3a;
  --blue:#2f9ad8;
  --blue-dark:#1a7fbf;
  --text:#333;
  --muted:#8a8a8a;
  --line:#d8d8d8;
  --page:#fafafa;
}
*{margin:0;padding:0;box-sizing:border-box}
html,body{width:1200px;height:1036px;overflow:hidden}
body{position:relative;background:var(--page);font-family:Arial,Helvetica,sans-serif;color:var(--text)}
.cond{font-family:"Roboto Condensed",Arial,sans-serif}
.top-bar{position:absolute;left:0;top:0;width:1200px;height:44px;background:linear-gradient(#555,var(--bar-dark));color:#fff}
.top-phone{position:absolute;left:820px;top:13px;font-size:16px;font-weight:700;display:flex;align-items:center;gap:8px}
.top-divider{position:absolute;left:936px;top:8px;width:1px;height:28px;background:#888}
.top-contact{position:absolute;left:950px;top:13px;font-size:16px;font-weight:700}
.brand{position:absolute;left:166px;top:68px;color:var(--blue);font-size:24px;font-weight:700;line-height:27px;white-space:nowrap}
.nav{position:absolute;right:173px;top:92px;display:flex;font-size:16px;list-style:none}
.nav li{padding:0 14px;border-left:1px solid #555;line-height:14px;color:#222}
.nav li:first-child{border-left:0;color:var(--blue)}
.nav li:last-child{padding-right:0}
.hero{position:absolute;left:166px;top:159px;width:868px;height:386px;background:linear-gradient(90deg,#cfd6de,#e8ecef 45%,#d9c9bd 75%,#eceae6);box-shadow:0 0 6px rgba(0,0,0,.35)}
.arc{position:absolute;left:0;top:500px}
.welcome{position:absolute;left:0;width:1200px;top:546px;text-align:center;font-size:16px;font-weight:700;letter-spacing:.5px}
.welcome span{color:var(--blue)}
.intro{position:absolute;left:300px;top:580px;width:600px;text-align:center;font-size:11.5px;line-height:16px;color:#555}
.rule{position:absolute;top:673px;height:4px;border-top:1px solid var(--line);border-bottom:1px solid var(--line)}
.upload{position:absolute;left:497px;top:657px;width:207px;height:37px;background:linear-gradient(#4fb1e6,var(--blue-dark));border:2px solid #9fd3f0;outline:1px solid var(--blue);color:#fff;font-size:24px;text-align:center;line-height:33px;letter-spacing:.5px}
.tab{position:absolute;height:28px;background:linear-gradient(#4fb1e6,var(--blue-dark));border:2px solid #bfe2f5;border-bottom:0;border-radius:5px 5px 0 0;color:#fff;font-size:13px;font-weight:700;text-align:center;line-height:26px;letter-spacing:.5px;white-space:nowrap}
.panel{position:absolute;top:754px;height:196px;border:1px solid var(--line);background:#fff;border-radius:3px}
.panel-inner{position:absolute;inset:7px;border:1px dashed #e2e2e2}
.card-img{position:absolute;top:27px;width:212px;height:76px;background:linear-gradient(135deg,#8a9aa8,#d8dde2 55%,#6e7f90)}
.card-text{position:absolute;top:117px;width:200px;font-size:11.5px;line-height:16px;color:#555;text-align:justify}
.arrow{position:absolute;top:88px}
.news{list-style:none;position:absolute;left:24px;top:20px;width:248px}
.news li{font-size:11.5px;line-height:16px;text-align:justify;color:var(--muted);margin-bottom:5px;position:relative}
.news li:first-child{color:#444}
.news li::before{content:"";position:absolute;left:-13px;top:6px;width:4px;height:4px;background:#999}
.footer{position:absolute;left:0;top:977px;width:1200px;height:59px;background:var(--bar);color:#fff}
.foot-nav{position:absolute;left:176px;top:13px;display:flex;list-style:none;font-size:11px;font-weight:700;letter-spacing:.5px}
.foot-nav li{padding:0 10px;border-left:1px solid #ccc;line-height:10px}
.foot-nav li:first-child{padding-left:0;border-left:0}
.copy{position:absolute;left:176px;top:31px;font-size:11px;font-weight:700;letter-spacing:.3px}
.social{position:absolute;top:14px;width:22px;height:22px;background:#dfe6ec;border-radius:3px}
</style>
</head>
<body>
<header class="top-bar cond">
  <div class="top-phone">
    <svg width="16" height="14" viewBox="0 0 16 14"><path d="M1 5c0-3 14-3 14 0v2h-4V5H5v2H1z M3 8h10l1 5H2z" fill="#fff"/></svg>
    5550192834
  </div>
  <div class="top-divider"></div>
  <div class="top-contact">CONTACT US</div>
</header>

<div class="brand cond">BRIGHTLEAF<br>PRACTICE PARTNERS, INC</div>

<ul class="nav cond">
  <li>HOME</li><li>ABOUT US</li><li>SERVICES</li><li>HELP</li><li>RESUME/BIO</li><li>LOCATION</li>
</ul>

<div class="hero" role="img" aria-label="Photo of a nurse and a doctor examining a smiling baby held by its mother in a bright clinic"></div>

<svg class="arc" width="1200" height="100" viewBox="0 0 1200 100">
  <path d="M0 92 Q600 -40 1200 92 Q600 -20 0 92z" fill="var(--blue)"/>
</svg>

<h1 class="welcome cond">WELCOME TO <span>BRIGHTLEAF PRACTICE PARTNERS, INC</span></h1>
<p class="intro">Lorem ipsum dolor sit amet, consectetur adipiscing elit. Integer diam arcu, imperdiet a consequat at, faucibus et elit. Quisque sit amet est ut tortor suscipit ultrices non nec mi. Donec euismod ipsum ultricies risus adipiscing auctor. Duis eget dui quis enim luctus faucibus id id velit. Pellentesque habitant morbi tristique senectus et netus et malesuada fames ac turpis egestas. Proin gravida dictum est, id suscipit lorem scelerisque sit amet. Duis luct</p>

<div class="rule" style="left:175px;width:312px"></div>
<div class="rule" style="left:714px;width:311px"></div>
<div class="upload cond">UPLOAD RESUME</div>

<div class="tab cond" style="left:195px;top:727px;width:174px">MARKETING &amp; MANAGEMENT</div>
<section class="panel" style="left:166px;width:551px">
  <div class="panel-inner"></div>
  <svg class="arrow" style="left:12px" width="16" height="22"><path d="M14 1 L2 11 L14 21z" fill="#ddd"/></svg>
  <div class="card-img" style="left:43px" role="img" aria-label="Photo of hands signing a business document"></div>
  <p class="card-text" style="left:49px">Lorem ipsum dolor sit amet, consectetur adipiscing elit. Integer diam arcu, imperdiet a consequat at, faucibus et eli</p>
  <div class="card-img" style="left:283px" role="img" aria-label="Photo of hands signing a business document"></div>
  <p class="card-text" style="left:289px">Lorem ipsum dolor sit amet, consectetur adipiscing elit. Integer diam arcu, imperdiet a consequat at, faucibus et eli</p>
  <svg class="arrow" style="left:521px" width="16" height="22"><path d="M2 1 L14 11 L2 21z" fill="#ddd"/></svg>
</section>

<div class="tab cond" style="left:814px;top:727px;width:96px">LATEST NEWS</div>
<section class="panel" style="left:749px;width:286px">
  <div class="panel-inner"></div>
  <ul class="news">
    <li>Lorem ipsum dolor sit amet, consectetur adipiscing elit. Integer diam arcu, imperdiet a consequat at, faucibus et eli</li>
    <li>Lorem ipsum dolor sit amet, consectetur adipiscing elit. Integer diam arcu, imperdiet a consequat at, faucibus et eli</li>
    <li>Lorem ipsum dolor sit amet, consectetur adipiscing elit. Integer diam arcu, imperdiet a consequat at, faucibus et eli</li>
  </ul>
</section>

<footer class="footer cond">
  <ul class="foot-nav">
    <li>HOME</li><li>SERVICES</li><li>HELP</li><li>LOCATION</li><li>PRIVACY POLICY</li><li>TERMS</li>
  </ul>
  <div class="copy">All Rights reserved© Brightleaf Practice Partners, Inc</div>
  <div class="social" style="left:957px"></div>
  <div class="social" style="left:993px"></div>
</footer>
</body>
</html>
```